Stationery Design Project

I am looking for stationary design for an automotive collision repair company. This needs to work with my business cards just designed here. I've attached. I need 8.5 x 11 stationary and corissponding envelopes. a jot tab note pad also. Our companies focus is very high end customer service driven . Our customer base is 35-65 middle to high income. Please include company name, logo, address, phone number, web address. The business card is two greys with green and white writing. I invision a light grey background with a darker grey band on it that contains the logo.
Updates

I justĀ 

Why is no one touching this project

Target Market(s)

60%. Women 40% men. Age 35-60

Industry/Entity Type

Automotive

Requirements
Must have
• Tie in with business cards. So it needs grey tones with green and white logo. Name, address, phone and web address. Must have 8.5 x 11 paper and envelopes.
Nice to have
• Jot tab notes

```html
<!DOCTYPE html>
<html lang="en">
<head>
<meta charset="utf-8">
<title>PanelRight Letterhead</title>
<link rel="stylesheet" href="https://fonts.googleapis.com/css2?family=Arimo:wght@400;700&display=swap">
<style>
  :root {
    --charcoal: #3a3638;
    --lime: #7dc242;
    --paper: #ffffff;
    --silver: #b9b9b9;
    --footer-text: #a9a9a9;
  }
  html, body {
    margin: 0;
    padding: 0;
    overflow: hidden;
    background: var(--paper);
  }
  .letterhead {
    position: relative;
    width: 927px;
    height: 1200px;
    background: var(--paper);
    overflow: hidden;
    font-family: "Arimo", Arial, sans-serif;
  }
  .header-band,
  .footer-band {
    position: absolute;
    left: 0;
    display: block;
  }
  .header-band { top: 0; }
  .footer-band { bottom: 0; }
  .brand-name {
    position: absolute;
    left: 107px;
    top: 74px;
    margin: 0;
    font-size: 44px;
    font-weight: 700;
    line-height: 1;
    color: var(--lime);
    letter-spacing: -0.5px;
  }
  .contact {
    position: absolute;
    right: 29px;
    top: 48px;
    text-align: right;
    font-size: 14.5px;
    line-height: 19px;
    color: var(--paper);
  }
  .contact .contact-name {
    color: var(--lime);
    font-size: 15.5px;
  }
  .web-address {
    position: absolute;
    left: 0;
    right: 0;
    top: 1168px;
    text-align: center;
    font-size: 15px;
    color: var(--footer-text);
  }
</style>
</head>
<body>
  <main class="letterhead">
    <svg class="header-band" width="927" height="175" viewBox="0 0 927 175" aria-hidden="true">
      <path d="M0 0 H927 V146 Q520 138 0 156 Z" fill="var(--charcoal)"/>
      <path d="M0 157 Q520 139 927 147 L927 150 Q520 144 0 162 Z" fill="var(--lime)"/>
    </svg>

    <p class="brand-name">PanelRight</p>

    <address class="contact">
      <div class="contact-name">Dana Kestrel</div>
      <div>208 Fender Lane Brightmoor 4117</div>
      <div>CA 90412.</div>
      <div>T: 555-010-0199</div>
    </address>

    <svg class="footer-band" width="927" height="100" viewBox="0 0 927 100" aria-hidden="true">
      <path d="M0 47 Q400 28 880 38 L927 30 V100 H0 Z" fill="var(--charcoal)"/>
      <path d="M470 38 Q700 -5 870 40 Q700 14 470 38 Z" fill="var(--silver)"/>
      <path d="M0 47 Q400 33 880 38 Q420 38 0 51 Z" fill="var(--silver)"/>
      <rect x="0" y="93" width="927" height="7" fill="var(--lime)"/>
    </svg>

    <div class="web-address">www.panelright.com</div>
  </main>
</body>
</html>
```